Building Design company needing a letterhead

We need a letter head for our Building Design company to send letters etc. to our clients, consultants, councils etc. We would like to see our logo used and company colours. I have attached our style guide and an example of our current letterheads. Top left we would like our logo, top right we would like the company details and at the footer we would like some sort of image/design etc. that suits our brand. I like the Torvik Design letterhead attached.

Target Market(s)

Professionals, Councils, Consultants, Mums & Dads

Industry/Entity Type

Architecture

Font styles to use
Other font styles liked:
• refer the design style guide

Colors
f37122
000000
1b1b1b

Requirements
Must have
• Must have the minimum of a logo, company details and footer
Nice to have
• An image/design made for the footer that would suite our brand and website at www.quarvedesign.com.au. Also it would be nice to include the GMKLE logo somewhere perhaps included in the footer.
Should not have
• Large images in the header. I just want the logo and company details.

```html
<!DOCTYPE html>
<html lang="en">
<head>
<meta charset="utf-8">
<title>Quarve Design – Letterhead</title>
<link rel="stylesheet" href="https://fonts.googleapis.com/css2?family=Michroma&family=Open+Sans:wght@400;600;700&display=swap">
<style>
  :root {
    --backdrop: #151515;
    --paper: #ffffff;
    --orange-deep: #e85a28;
    --orange-soft: #ed7e47;
    --ink: #1b1b1b;
    --watermark: #e9e7e7;
    --on-orange: #ffffff;
  }
  * { margin: 0; padding: 0; box-sizing: border-box; }
  html, body {
    width: 960px; height: 1200px; overflow: hidden;
    background: var(--backdrop);
  }
  .letterhead {
    position: absolute; left: 184px; top: 150px;
    width: 608px; height: 913px;
    background: var(--paper);
    overflow: hidden;
    font-family: "Open Sans", Arial, sans-serif;
  }
  .letterhead__shapes { position: absolute; inset: 0; width: 100%; height: 100%; }
  .brand {
    position: absolute; left: 44px; top: 48px;
    display: flex; align-items: center; gap: 10px;
  }
  .brand__mark { width: 34px; height: 34px; background: var(--orange-deep); }
  .brand__name {
    font-weight: 700; font-size: 21px; line-height: 1.05;
    letter-spacing: 1.5px; color: var(--ink); text-transform: uppercase;
  }
  .sender {
    position: absolute; right: 41px; top: 26px; text-align: right;
    font-family: "Michroma", "Arial", sans-serif; color: var(--on-orange);
    font-variant: small-caps; letter-spacing: 1.5px;
  }
  .sender__name { font-size: 10px; line-height: 13px; }
  .sender__role { font-size: 8.5px; line-height: 11px; }
  .watermark {
    position: absolute; left: 40px; top: 420px;
    transform: rotate(-27deg); transform-origin: left top;
    display: flex; align-items: center; gap: 24px;
  }
  .watermark__mark { width: 90px; height: 90px; background: var(--watermark); }
  .watermark__name {
    font-weight: 700; font-size: 62px; line-height: 1; letter-spacing: 4px;
    color: var(--watermark); text-transform: uppercase;
  }
  .address {
    position: absolute; left: 32px; top: 879px;
    font-size: 8.5px; color: var(--on-orange);
  }
  .contacts {
    position: absolute; right: 28px; top: 840px;
    list-style: none; text-align: right;
    font-size: 8.5px; line-height: 13px; color: var(--on-orange);
  }
  .contacts li { display: flex; justify-content: flex-end; align-items: center; gap: 5px; }
  .contacts svg { width: 8px; height: 8px; fill: var(--on-orange); }
</style>
</head>
<body>
  <main class="letterhead">
    <svg class="letterhead__shapes" viewBox="0 0 608 913" preserveAspectRatio="none" aria-hidden="true">
      <defs>
        <linearGradient id="band" x1="0" y1="0" x2="0" y2="1">
          <stop offset="0" stop-color="#e85a28"/>
          <stop offset="1" stop-color="#ed7e47"/>
        </linearGradient>
        <linearGradient id="band-foot" x1="0" y1="0" x2="0" y2="1">
          <stop offset="0" stop-color="#e85a28"/>
          <stop offset="0.5" stop-color="#ec7640"/>
          <stop offset="1" stop-color="#ed7e47"/>
        </linearGradient>
      </defs>
      <path class="header-band" fill="url(#band)"
        d="M0 0 H608 V75 C540 105 480 112 440 107 C330 98 260 60 200 30 C165 12 120 8 90 20 C50 35 20 50 0 68 Z"/>
      <path class="footer-band" fill="url(#band-foot)"
        d="M0 853 C250 868 500 835 608 761 V913 H0 Z"/>
    </svg>

    <div class="brand">
      <span class="brand__mark"></span>
      <span class="brand__name">Quarve<br>Design</span>
    </div>

    <div class="sender">
      <p class="sender__name">John Smith</p>
      <p class="sender__role">Designation</p>
    </div>

    <div class="watermark" aria-hidden="true">
      <span class="watermark__mark"></span>
      <span class="watermark__name">Quarve<br>Design</span>
    </div>

    <p class="address">Address Line1, Address Line2 Country -123456</p>

    <ul class="contacts">
      <li>123-456-7890
        <svg viewBox="0 0 10 10"><path d="M1 3 Q5 0 9 3 L8 4.5 L6.5 3.8 V3 H3.5 V3.8 L2 4.5 Z M2.5 5 H7.5 L8.5 9 H1.5 Z"/></svg></li>
      <li>123-456-7890
        <svg viewBox="0 0 10 10"><path d="M2 1 H7 V3 H9 V9 H1 V3 H2 Z M3 2 V4 H6 V2 Z M3 6 V7 H7 V6 Z"/></svg></li>
      <li>info@companyname.com
        <svg viewBox="0 0 10 10"><path d="M0.5 2 H9.5 V8 H0.5 Z M1.5 3 L5 5.5 L8.5 3 Z"/></svg></li>
      <li>www.companyname.com
        <svg viewBox="0 0 10 10"><path d="M6 1 L9 4 L7.5 5.5 L7 5 L8 4 L6 2 L5 3 L4.5 2.5 Z M4 9 L1 6 L2.5 4.5 L3 5 L2 6 L4 8 L5 7 L5.5 7.5 Z M3.5 6 L6 3.5 L6.5 4 L4 6.5 Z"/></svg></li>
    </ul>
  </main>
</body>
</html>
```